KVE Palliative Care Flyer

We need an A5 flyer designed for print on high quality card. The flyer will be placed on every seat at two Brindlewood Chamber Ensemble concerts dedicated to awareness raising of palliative care. We would like to have a flyer that uses our logo, and an image of a couple waltzing or in waltz hold. The final design should communicate the essence of palliative care which is that you matter to us, and you matter right to the very end of your life. "Putting life in the days, not days in the life".

Target Market(s)

Concert goers

Requirements
Must have
• Gentle Harbour Alliance SA logo

```html
<!DOCTYPE html>
<html lang="en">
<head>
<meta charset="utf-8">
<title>Gentle Harbour Alliance SA – Concert Flyer</title>
<link href="https://fonts.googleapis.com/css2?family=Overlock:wght@400;700&display=swap" rel="stylesheet">
<style>
  :root{
    --night:#2b2a5c;
    --night-deep:#1d1c45;
    --violet:#4a3f7c;
    --ivory:#ffffff;
    --ink:#1e1e1e;
    --panel-top:#d9d9d9;
    --panel-bottom:#fbfbfb;
    --brand-teal:#2aa6c9;
    --brand-grey:#6d6e70;
    --gown:#e9e3dc;
  }
  *{box-sizing:border-box;margin:0;padding:0}
  html,body{width:1200px;height:851px;overflow:hidden;background:var(--ivory)}
  body{font-family:"Overlock",sans-serif;position:relative}

  .flyer{position:relative;width:1200px;height:851px}

  /* Left face */
  .front{position:absolute;left:0;top:0;width:600px;height:851px;overflow:hidden;color:var(--ivory)}
  .front-backdrop{position:absolute;inset:0;
    background:
      radial-gradient(ellipse at 30% 20%, #8c86b8 0%, rgba(140,134,184,0) 45%),
      radial-gradient(ellipse at 80% 55%, #5a5290 0%, rgba(90,82,144,0) 50%),
      linear-gradient(180deg,var(--violet) 0%,var(--night) 55%,var(--night-deep) 100%);}
  .dancers{position:absolute;left:0;top:95px;width:380px;height:470px;
    background:radial-gradient(ellipse at 45% 55%, var(--gown) 0%, rgba(233,227,220,.55) 40%, rgba(233,227,220,0) 72%);}

  .headline{position:absolute;left:10px;top:12px;width:250px;text-align:center;
    font-size:29px;line-height:34px;font-weight:400;text-shadow:0 0 6px #000,0 0 2px #000}
  .headline strong{font-weight:700}

  .logo-tab{position:absolute;left:268px;top:14px;width:340px;height:72px;background:var(--ivory);
    border-radius:14px 0 0 14px;display:flex;align-items:center;gap:12px;padding-left:22px}
  .brand-dot{width:34px;height:34px;border-radius:50%;background:var(--brand-teal);flex:none}
  .brand-name{font-size:21px;line-height:22px;font-weight:700;color:var(--brand-grey)}

  .tagline{position:absolute;left:315px;top:132px;font-size:25px;line-height:26px;text-shadow:0 0 4px #000}
  .thanks{position:absolute;left:372px;top:206px;width:210px;font-size:17px;line-height:26px;font-weight:700}
  .intro{position:absolute;left:341px;top:404px;width:226px;font-size:17px;line-height:24px;text-align:justify}
  .body-copy{position:absolute;left:42px;top:560px;width:526px;font-size:16.5px;line-height:20.5px;text-align:justify}
  .body-copy p+p{margin-top:14px}

  /* Right face */
  .back{position:absolute;left:600px;top:0;width:600px;height:851px}
  .message{position:absolute;left:40px;top:47px;width:520px;height:621px;border-radius:16px;
    background:linear-gradient(180deg,var(--panel-top) 0%,var(--panel-bottom) 100%);
    padding:12px 20px 0 22px;color:var(--ink);font-size:17.5px;line-height:28.5px;text-align:justify}
  .message p+p{margin-top:28px}

  .footer-brand{position:absolute;left:160px;top:690px;display:flex;align-items:center;gap:12px}
  .contact{position:absolute;left:0;top:756px;width:600px;text-align:center;font-size:15px;line-height:23px;color:var(--ink)}
</style>
</head>
<body>
<main class="flyer">
  <section class="front">
    <div class="front-backdrop" role="img" aria-label="Night sky lit with fireworks"></div>
    <div class="dancers" role="img" aria-label="Couple in evening dress dancing the waltz"></div>

    <h1 class="headline">What does the<br><strong>VIENNESE WALTZ</strong><br>have to do with<br>Palliative Care?</h1>

    <div class="logo-tab">
      <span class="brand-dot"></span>
      <span class="brand-name">Gentle Harbour<br>Alliance SA</span>
    </div>

    <p class="tagline">Putting life in the days,<br>not days in the life.</p>

    <p class="thanks">The Gentle Harbour Alliance South Australia Inc. is grateful to the Brindlewood Chamber Ensemble for its welcome to this partnership concert.</p>

    <p class="intro">It may seem strange that the energy and life of the Viennese waltz could be linked with the situation of those who have advanced and terminal illness.</p>

    <div class="body-copy">
      <p>The waltz is a smooth and progressive dance for a ballroom or folk-gathering; it calls for partnership, expertise and the assistance of music, best offered by a team of instrumentalists, none better that our KVE.</p>
      <p>Palliative care also seeks to be smooth and progressive in its offer of care – always available, responsive, and in partnership with the patient and family. It calls for medical and nursing expertise, but just as each waltzing couple has its own individual style, palliative care seeks to be patient-centred, offering the support that the patient and family see as most appropriate for them.</p>
    </div>
  </section>

  <section class="back">
    <div class="message">
      <p>Some persons feel they cannot dance; many feel unable to approach the prospect of death and dying.<br>Just as everyone can learn to waltz, everyone should be prepared to consider the circumstances of major illness and the treat of dying – we never know its timing.</p>
      <p>And we should be prepared to start a conversation with those close to us about how we wish a serious illness to be managed. It will serve to dispel anxieties and fears and will facilitate communication in crisis situations. South Australia is preparing Advance Care Directives legislation that will encourage us all to do this, and write it down.</p>
      <p>Tonight we affirm both the spirit-lifting rhythm of the waltz, and the heart warming work of palliative care.</p>
      <p>Everyone should understand also what palliative care can offer for make the ‘dance with death’ something not to be feared. It is not about helping to die, more about ensuring comfort and fostering patience, courage and love; that are the values of life itself. The Gentle Harbour Alliance will welcome your queries and assistance.</p>
    </div>

    <div class="footer-brand">
      <span class="brand-dot"></span>
      <span class="brand-name">Gentle Harbour<br>Alliance SA</span>
    </div>

    <address class="contact" style="font-style:normal">
      Suite 4c 18-22 Wattle Grove Road Kestrel Park SA 5071<br>
      PO Box 912 Marlowe SA 5071 &nbsp;|&nbsp; P: 8350 2719<br>
      E: hello@gentleharbour.example &nbsp;W: www.gentleharbour.example
    </address>
  </section>
</main>
</body>
</html>
```